Email Notification & Marketing Templates

I want to start with something like a newsletter or informational email, but i need Top Tips to Detect Phishing Scams. Something that i can send to users so they can follow it when receiving or exchanging emails. I will also need promotional items for my company that i can send to customers as well. It can be based on on our website PLVORIX.COM

Will also need:
newsletters
announcements
marketing emails
alerts
security notifications

Examples:Items such as Security Awareness Poster Series
Phishing Awareness
Password Security
Email Attachments
QR Code scams
Public WiFi safety

```html
<!DOCTYPE html>
<html lang="en">
<head>
<meta charset="utf-8">
<title>Top Tips to Detect Phishing Scams – Plvorix Networks</title>
<link href="https://fonts.googleapis.com/css2?family=Montserrat:wght@400;500;600;700;800&display=swap" rel="stylesheet">
<style>
  :root {
    --page-bg: #f6f6f6;
    --card-bg: #ffffff;
    --card-edge: #e4e4e4;
    --band-bg: #efefef;
    --ink: #111111;
    --body-ink: #2a2a2a;
    --muted: #6b6b6b;
    --brand-green: #3d9a1f;
    --brand-green-light: #5bbf2a;
    --brand-green-dark: #2f7d14;
    --alert-red: #e2463a;
    --alert-orange: #f08a32;
    --icon-grey: #8a8f96;
  }
  * { box-sizing: border-box; margin: 0; padding: 0; }
  html, body {
    width: 1200px;
    height: 1200px;
    overflow: hidden;
    background: var(--page-bg);
    font-family: "Montserrat", Arial, sans-serif;
    color: var(--ink);
  }
  .email-card {
    position: absolute;
    left: 120px;
    top: 0;
    width: 960px;
    height: 1200px;
    background: var(--card-bg);
    border-left: 1px solid var(--card-edge);
    border-right: 1px solid var(--card-edge);
  }
  .brand {
    position: absolute;
    left: 48px;
    top: 72px;
    display: flex;
    align-items: center;
    gap: 14px;
  }
  .brand-square {
    width: 38px;
    height: 38px;
    background: var(--brand-green);
  }
  .brand-name {
    font-size: 52px;
    font-weight: 800;
    color: var(--brand-green);
    letter-spacing: 1px;
    line-height: 1;
  }
  .hero-art {
    position: absolute;
    left: 595px;
    top: 62px;
    width: 330px;
    height: 330px;
    border-radius: 50%;
    background: radial-gradient(circle at 50% 45%, #6cc43a 0%, #3f9d22 38%, #f7d8d6 62%, #ffffff 78%);
  }
  .headline {
    position: absolute;
    left: 48px;
    top: 262px;
    font-size: 63px;
    font-weight: 700;
    line-height: 73px;
    color: var(--ink);
    letter-spacing: -0.5px;
  }
  .tips-band {
    position: absolute;
    left: 0;
    top: 448px;
    width: 958px;
    height: 522px;
    background: var(--band-bg);
    padding: 40px 0 0 44px;
  }
  .tip {
    display: flex;
    align-items: flex-start;
    height: 88px;
  }
  .tip-icon {
    width: 66px;
    height: 66px;
    flex: none;
    margin-right: 20px;
    margin-top: -2px;
  }
  .tip-title {
    font-size: 26px;
    font-weight: 700;
    line-height: 30px;
    color: var(--ink);
  }
  .tip-text {
    font-size: 22px;
    font-weight: 500;
    line-height: 28px;
    color: var(--body-ink);
    max-width: 760px;
  }
  .tip-long { height: 116px; }
  .cta-button {
    position: absolute;
    left: 45px;
    top: 1010px;
    width: 870px;
    height: 68px;
    border-radius: 7px;
    background: linear-gradient(180deg, var(--brand-green-light) 0%, var(--brand-green) 55%, var(--brand-green-dark) 100%);
    color: #ffffff;
    font-size: 30px;
    font-weight: 700;
    display: flex;
    align-items: center;
    justify-content: center;
    text-decoration: none;
  }
  .footer {
    position: absolute;
    left: 0;
    top: 1126px;
    width: 958px;
    text-align: center;
    font-size: 20px;
    font-weight: 400;
    color: var(--muted);
  }
  .footer a { color: var(--muted); text-decoration: underline; }
</style>
</head>
<body>
<main class="email-card">
  <header class="brand">
    <span class="brand-square"></span>
    <span class="brand-name">PLVORIX</span>
  </header>

  <div class="hero-art" role="img" aria-label="Illustration of a green security shield with an envelope, fishing hook and warning signs"></div>

  <h1 class="headline">Top Tips to Detect<br>Phishing Scams</h1>

  <section class="tips-band">
    <div class="tip">
      <svg class="tip-icon" viewBox="0 0 66 66" aria-hidden="true">
        <circle cx="27" cy="27" r="18" fill="#fff" stroke="var(--icon-grey)" stroke-width="5"/>
        <line x1="40" y1="40" x2="56" y2="56" stroke="#555" stroke-width="7" stroke-linecap="round"/>
        <path d="M27 15 L38 34 H16 Z" fill="var(--alert-red)"/>
        <rect x="25.8" y="21" width="2.4" height="7" fill="#fff"/>
        <circle cx="27" cy="31" r="1.4" fill="#fff"/>
      </svg>
      <div>
        <h2 class="tip-title">Suspicious Sender Address</h2>
        <p class="tip-text">Check for misspelled domains or unfamiliar contacts.</p>
      </div>
    </div>

    <div class="tip">
      <svg class="tip-icon" viewBox="0 0 66 66" aria-hidden="true">
        <circle cx="29" cy="31" r="23" fill="#fff" stroke="var(--alert-red)" stroke-width="5"/>
        <line x1="29" y1="31" x2="29" y2="17" stroke="#333" stroke-width="3" stroke-linecap="round"/>
        <line x1="29" y1="31" x2="39" y2="31" stroke="#333" stroke-width="3" stroke-linecap="round"/>
        <circle cx="48" cy="48" r="11" fill="var(--alert-red)"/>
        <rect x="46.6" y="41" width="2.8" height="9" fill="#fff"/>
        <circle cx="48" cy="53.5" r="1.6" fill="#fff"/>
      </svg>
      <div>
        <h2 class="tip-title">Urgent or Threatening Language</h2>
        <p class="tip-text">Be wary of emails demanding immediate action or payment.</p>
      </div>
    </div>

    <div class="tip tip-long">
      <svg class="tip-icon" viewBox="0 0 66 66" aria-hidden="true">
        <rect x="20" y="8" width="14" height="26" rx="7" fill="none" stroke="var(--icon-grey)" stroke-width="5" transform="rotate(40 27 21)"/>
        <rect x="10" y="28" width="14" height="26" rx="7" fill="none" stroke="var(--icon-grey)" stroke-width="5" transform="rotate(40 17 41)"/>
        <line x1="40" y1="4" x2="42" y2="10" stroke="#333" stroke-width="2"/>
        <line x1="46" y1="8" x2="43" y2="13" stroke="#333" stroke-width="2"/>
        <path d="M48 38 L61 60 H35 Z" fill="var(--alert-red)"/>
        <rect x="46.8" y="45" width="2.4" height="8" fill="#fff"/>
        <circle cx="48" cy="56" r="1.4" fill="#fff"/>
      </svg>
      <div>
        <h2 class="tip-title">Fake Links and Attachments</h2>
        <p class="tip-text">Hover over links to see the actual destination. Never download unexpected files.</p>
      </div>
    </div>

    <div class="tip">
      <svg class="tip-icon" viewBox="0 0 66 66" aria-hidden="true">
        <path d="M16 28 V19 a13 13 0 0 1 26 0 V28" fill="none" stroke="#555" stroke-width="5"/>
        <rect x="8" y="27" width="42" height="30" rx="4" fill="#5bb33a"/>
        <circle cx="29" cy="40" r="4" fill="#2f6e1a"/>
        <circle cx="50" cy="52" r="11" fill="var(--alert-red)"/>
        <path d="M45.5 47.5 L54.5 56.5 M54.5 47.5 L45.5 56.5" stroke="#fff" stroke-width="2.6" stroke-linecap="round"/>
      </svg>
      <div>
        <h2 class="tip-title">Unusual Requests for Info</h2>
        <p class="tip-text">Legitimate companies won't ask for sensitive data via email.</p>
      </div>
    </div>

    <div class="tip">
      <svg class="tip-icon" viewBox="0 0 66 66" aria-hidden="true">
        <circle cx="29" cy="30" r="23" fill="#fff" stroke="#c9c9c9" stroke-width="3"/>
        <path d="M21 23 a8 8 0 1 1 11 7.5 c-2.5 1 -3 2.5 -3 5" fill="none" stroke="var(--alert-orange)" stroke-width="4.5" stroke-linecap="round"/>
        <circle cx="29" cy="42" r="2.6" fill="var(--alert-orange)"/>
        <path d="M48 40 L61 62 H35 Z" fill="var(--alert-red)"/>
        <rect x="46.8" y="47" width="2.4" height="8" fill="#fff"/>
        <circle cx="48" cy="58" r="1.4" fill="#fff"/>
      </svg>
      <div>
        <h2 class="tip-title">Too Good to Be True Offers</h2>
        <p class="tip-text">If it seems suspicious, it likely is. Verify through official channels.</p>
      </div>
    </div>
  </section>

  <a class="cta-button" href="#">Stay Protected</a>

  <footer class="footer">Plvorix Networks | www.plvorix.com | <a href="#">Unsubscribe</a></footer>
</main>
</body>
</html>
```